Cover design for inventory booklets

As a company we have used a front cover to all our reports which need to include specific information about each property
We therefore need an A4 design design which must allow for inclusion of of the following editable elements through Microsoft Word although I am happy to embed graphical content into Word if not done as part of design process:
Property picture (or pictures if design allows)
Property address
Property size
Agent name (can include logo insert as well if you want)
Job type
Job date
We would like something which appears professional but also acts as a sales tool for the company and repeat business so inclusion of contact details in some form is essential
Style and colours should be derived and be reasonably consistent with those found in our website potentially included the blue tones from the logo and the green of the website as contrast at http://www.quillbrookstays.co.uk/ although please do not let this constrain the designs submitted as we will provide feedback as needed
Target Market(s)
Primary - Letting Agents, Secondary - Landlords and Tenants
Industry/Entity Type
Business

```html
<!DOCTYPE html>
<html lang="en">
<head>
<meta charset="utf-8">
<title>Inventory Cover</title>
<link href="https://fonts.googleapis.com/css2?family=Open+Sans:wght@300;400;700&display=swap" rel="stylesheet">
<style>
  :root {
    --backdrop: #e9eaec;
    --navy: #1f2b86;
    --royal: #34459f;
    --brand-green: #6cc24a;
    --sheet: #f4f5f6;
    --box: #eceef1;
    --ink: #2f3035;
    --white: #ffffff;
  }
  * { margin: 0; padding: 0; box-sizing: border-box; }
  html, body { width: 1200px; height: 900px; overflow: hidden; }
  body {
    background: var(--backdrop);
    font-family: "Open Sans", Arial, sans-serif;
    position: relative;
  }
  .cover {
    position: absolute;
    left: 303px; top: 30px;
    width: 594px; height: 840px;
    background: var(--sheet);
    box-shadow: 0 6px 20px rgba(0,0,0,0.18);
    overflow: hidden;
  }
  .cover-backdrop {
    position: absolute; inset: 0;
    background: linear-gradient(160deg, #e3e6e8 0%, #d9dcd6 35%, #e6e1dc 60%, #dfe3e0 100%);
    opacity: 0.75;
  }
  .property-frame {
    position: absolute;
    left: 28px; top: 28px; width: 538px; height: 320px;
    background: var(--navy);
    border-radius: 14px;
  }
  .property-photo {
    position: absolute;
    left: 14px; top: 14px; right: 14px; bottom: 14px;
    border: 1px solid var(--brand-green);
    background: linear-gradient(180deg, #1e6fd6 0%, #4f9ae6 38%, #f2f0e6 52%, #d9d0b4 70%, #5da33f 85%, #3a7f2b 100%);
  }
  .footer-band {
    position: absolute; left: 0; top: 0;
    width: 594px; height: 840px;
  }
  .inventory-box {
    position: absolute;
    left: 180px; top: 364px; width: 360px; height: 234px;
    background: var(--box);
    box-shadow: 0 2px 6px rgba(0,0,0,0.12);
  }
  .inventory-heading {
    height: 56px;
    background: linear-gradient(180deg, var(--royal) 0%, var(--navy) 100%);
    color: var(--white);
    font-weight: 700;
    font-size: 18px;
    letter-spacing: 0.5px;
    display: flex; align-items: center;
    padding-left: 22px;
    text-transform: uppercase;
  }
  .inventory-details {
    text-align: center;
    color: var(--ink);
    font-weight: 400;
    font-size: 18px;
    line-height: 23px;
    padding-top: 12px;
  }
  .inventory-details p + p { margin-top: 12px; }
  .agent-credit {
    position: absolute;
    right: 24px; top: 645px;
    text-align: right;
    color: var(--white);
    font-weight: 700;
    font-size: 17px;
    line-height: 23px;
  }
  .brand-block {
    position: absolute;
    left: 34px; top: 748px;
    color: var(--white);
  }
  .brand-name {
    display: flex; align-items: center; gap: 10px;
    font-weight: 400;
    font-size: 24px;
    letter-spacing: 1px;
    text-transform: uppercase;
  }
  .brand-mark {
    width: 14px; height: 14px;
    background: var(--white);
  }
  .brand-web {
    margin-top: 4px;
    padding-left: 24px;
    font-size: 12px;
    font-weight: 400;
    letter-spacing: 0.3px;
  }
</style>
</head>
<body>
  <main class="cover">
    <div class="cover-backdrop" role="img" aria-label="Faded aerial photograph of town rooftops and streets"></div>

    <section class="property-frame">
      <div class="property-photo" role="img" aria-label="Photograph of the property: white villa with pool, palm trees and lawn under a blue sky"></div>
    </section>

    <svg class="footer-band" viewBox="0 0 594 840" aria-hidden="true">
      <defs>
        <linearGradient id="bandFill" x1="0" y1="1" x2="1" y2="0">
          <stop offset="0" stop-color="#1d2a84"/>
          <stop offset="0.6" stop-color="#27358f"/>
          <stop offset="1" stop-color="#3a4ca6"/>
        </linearGradient>
      </defs>
      <path d="M0 740 C250 700 450 620 594 560 L594 730 Q300 840 0 840 Z" fill="url(#bandFill)"/>
      <path d="M594 730 Q300 840 0 840" fill="none" stroke="var(--brand-green)" stroke-width="5"/>
      <path d="M40 790 C250 760 440 690 594 620" fill="none" stroke="#ffffff" stroke-opacity="0.18" stroke-width="2"/>
    </svg>

    <section class="inventory-box">
      <h1 class="inventory-heading">Inventory of Content</h1>
      <div class="inventory-details">
        <p>24 Marlow Court<br>Ashby Lane<br>Surrey KT12 4LP</p>
        <p>2 Bedrooms Furnished Flat</p>
        <p>Checkout<br>12 September 2012</p>
      </div>
    </section>

    <p class="agent-credit">On Beharf of<br>Fernhill Lettings</p>

    <div class="brand-block">
      <div class="brand-name"><span class="brand-mark"></span>Quillbrook Stays</div>
      <p class="brand-web">www.quillbrookstays.co.uk</p>
    </div>
  </main>
</body>
</html>
```